FB and Youtube banner design for HVAC company

I would like an appealing site page banner for business page on Facebook (851w x 315h pixels) and one for youtube (2560w x 1440h pixels) for hvac company. Business card design and logo are attached. Company name is Bright Meadow Air Conditioning, Refrigeration, and Heating.

NOTE: I put the business cards and log up to see some of the artwork the company is using. It's not to replicate that in the banner images.

Target Market(s)

Interested business and homeowner visitors to Facebook business page and youtube channel page.

Industry/Entity Type

Hvac

Font styles to use
Sans Serif

Requirements
Must have
• See logo for color scheme.
Should not have
• This should not look like a business card. Think of what is typically the banner on a facebook business page and youtube channel.

```html
<!DOCTYPE html>
<html lang="en">
<head>
<meta charset="utf-8">
<title>Bright Meadow – Channel Banner</title>
<link rel="stylesheet" href="https://fonts.googleapis.com/css2?family=Montserrat:wght@600;800&display=swap">
<style>
  :root {
    --blue-deep: #1710a6;
    --blue-mid: #1f1cb8;
    --blue-light: #2e34c8;
    --blue-glow: #3a45d4;
    --orange: #ff6a13;
    --white: #ffffff;
    --link-bar: #6e6e78;
    --link-text: #f2f2f2;
  }
  html, body {
    margin: 0;
    padding: 0;
    overflow: hidden;
    background: var(--white);
  }
  .banner {
    position: relative;
    width: 1200px;
    height: 196px;
    overflow: hidden;
    background: var(--blue-deep);
    font-family: "Montserrat", Arial, sans-serif;
  }
  .banner__waves {
    position: absolute;
    inset: 0;
    width: 1200px;
    height: 196px;
  }
  .brand {
    position: absolute;
    left: 482px;
    top: 57px;
    width: 250px;
    height: 100px;
  }
  .brand__dot {
    position: absolute;
    left: 0;
    top: 6px;
    width: 68px;
    height: 68px;
    border-radius: 50%;
    background: var(--orange);
  }
  .brand__name {
    position: absolute;
    left: 80px;
    top: 2px;
    margin: 0;
    color: var(--white);
    font-weight: 800;
    font-size: 33px;
    line-height: 38px;
    letter-spacing: 0.5px;
    text-transform: uppercase;
  }
  .brand__services {
    position: absolute;
    left: 0;
    top: 84px;
    width: 246px;
    margin: 0;
    color: var(--white);
    font-weight: 600;
    font-size: 9.6px;
    letter-spacing: 0.6px;
    text-align: center;
    white-space: nowrap;
    text-transform: uppercase;
  }
  .links {
    position: absolute;
    left: 1000px;
    top: 158px;
    width: 190px;
    height: 25px;
    background: var(--link-bar);
    display: flex;
    align-items: center;
    gap: 6px;
    padding: 0 8px;
    box-sizing: border-box;
  }
  .links__site-dot {
    width: 11px;
    height: 11px;
    border-radius: 50%;
    background: #2b2b30;
  }
  .links__site {
    color: var(--link-text);
    font-weight: 600;
    font-size: 8.5px;
    margin-right: auto;
  }
  .links__icon {
    width: 11px;
    height: 11px;
    border-radius: 2px;
    background: #c9c9d2;
  }
</style>
</head>
<body>
  <div class="banner">
    <svg class="banner__waves" viewBox="0 0 1200 196" aria-hidden="true">
      <rect width="1200" height="196" fill="var(--blue-deep)"/>
      <path d="M0 0 H1200 V60 C1000 20 760 10 560 40 C360 70 160 90 0 70 Z" fill="var(--blue-mid)"/>
      <path d="M0 34 C180 70 380 44 600 22 C800 4 980 10 1200 40 V0 H0 Z" fill="var(--blue-light)" opacity="0.55"/>
      <path d="M0 52 C200 80 420 58 640 34 C840 14 1020 22 1200 60 V68 C1020 32 840 26 640 46 C420 70 200 92 0 62 Z" fill="var(--blue-glow)" opacity="0.5"/>
      <path d="M760 196 C920 170 1060 130 1200 70 V196 Z" fill="var(--blue-mid)"/>
      <path d="M880 196 C1010 176 1110 150 1200 110 V126 C1110 162 1010 186 920 196 Z" fill="var(--blue-glow)" opacity="0.6"/>
    </svg>

    <div class="brand">
      <span class="brand__dot" aria-hidden="true"></span>
      <h1 class="brand__name">Bright<br>Meadow</h1>
      <p class="brand__services">Air Conditioning - Refrigeration - Heating</p>
    </div>

    <div class="links">
      <span class="links__site-dot" aria-hidden="true"></span>
      <span class="links__site">brightmeadowair.com</span>
      <span class="links__icon" aria-hidden="true"></span>
      <span class="links__icon" aria-hidden="true"></span>
      <span class="links__icon" aria-hidden="true"></span>
      <span class="links__icon" aria-hidden="true"></span>
    </div>
  </div>
</body>
</html>
```